Business Card Design

I am a GP with interest in Dermatology and Aesthetic Medicin, performing Botulinum Toxin Type A and Dermal Fillers treatmets in Cosmetic Dermatology clinic.

I am looking for a white colour, good quality white paper card may be of some special texture with black calligraphic writing but easy to read and not to wiggly- professional- looking.

Really appreciate your help.

Halyna

Cosmetic Dermatology Clinic

Dr Halyna Korbutiak, MBBS, MRCGP, DPD

Tel: 07841 615 092
halyna@medmailbox.org.uk

```html
<!DOCTYPE html>
<html lang="en">
<head>
<meta charset="utf-8">
<title>Cosmetic Dermatology Clinic – Business Card</title>
<link rel="stylesheet" href="https://fonts.googleapis.com/css2?family=Open+Sans:wght@400;600&family=Yesteryear&display=swap">
<style>
  :root {
    --backdrop: #d3d3d5;
    --teal: #43b2bf;
    --white: #ffffff;
    --ink: #2b2b2b;
    --ink-soft: #4a4a4a;
    --card-shadow: rgba(0, 0, 0, 0.28);
  }
  * { box-sizing: border-box; margin: 0; padding: 0; }
  html, body {
    width: 883px;
    height: 1200px;
    overflow: hidden;
    background: var(--backdrop);
    font-family: "Open Sans", Arial, sans-serif;
  }
  .card-stack {
    position: absolute;
    left: 141px;
    top: 222px;
    width: 600px;
  }
  .card {
    position: relative;
    width: 600px;
    height: 336px;
    box-shadow: 0 6px 14px -4px var(--card-shadow);
  }
  .card + .card { margin-top: 28px; }
  .card--front { background: var(--teal); }
  .card--back { background: var(--white); }

  .clinic-name {
    display: flex;
    align-items: center;
    gap: 10px;
    font-family: "Open Sans", Arial, sans-serif;
    font-weight: 600;
    font-size: 22px;
    letter-spacing: 0.2px;
    white-space: nowrap;
  }
  .clinic-name__dot {
    width: 12px;
    height: 12px;
    border-radius: 50%;
    background: currentColor;
    flex: none;
  }
  .card--front .clinic-name {
    position: absolute;
    right: 30px;
    bottom: 36px;
    color: var(--white);
  }
  .card--back .clinic-name {
    position: absolute;
    left: 38px;
    top: 108px;
    color: var(--teal);
  }

  .holder {
    position: absolute;
    right: 28px;
    top: 190px;
    text-align: right;
  }
  .holder__name {
    font-family: "Yesteryear", cursive;
    font-size: 27px;
    line-height: 1;
    color: var(--ink);
  }
  .holder__credentials {
    margin-top: 4px;
    font-size: 15px;
    color: var(--ink-soft);
  }
  .divider {
    position: absolute;
    left: 36px;
    top: 240px;
    width: 384px;
    height: 1.5px;
    background: var(--teal);
  }
  .contact-list {
    position: absolute;
    left: 36px;
    top: 262px;
    list-style: none;
    font-size: 15px;
    line-height: 22px;
    color: var(--ink);
  }
  .contact-list li {
    display: flex;
    align-items: center;
    gap: 9px;
  }
  .contact-list svg {
    width: 12px;
    height: 12px;
    fill: var(--teal);
    flex: none;
  }
</style>
</head>
<body>
  <main class="card-stack">
    <section class="card card--front" aria-label="Card front">
      <div class="clinic-name"><span class="clinic-name__dot"></span>Cosmetic Dermatology Clinic</div>
    </section>

    <section class="card card--back" aria-label="Card back">
      <div class="clinic-name"><span class="clinic-name__dot"></span>Cosmetic Dermatology Clinic</div>

      <div class="holder">
        <p class="holder__name">Dr Halyna Korbutiak</p>
        <p class="holder__credentials">MBBS, MRCGP, DPD</p>
      </div>

      <div class="divider"></div>

      <ul class="contact-list">
        <li>
          <svg viewBox="0 0 12 12" aria-hidden="true"><path d="M1 3.2C1 2 2 1 3.2 1h5.6C10 1 11 2 11 3.2v.8H8.4V3H3.6v1H1z"/><path d="M2 5h8l1 5.5H1zM6 6.3a1.6 1.6 0 1 0 0 3.2 1.6 1.6 0 0 0 0-3.2z"/></svg>
          07841 615 092
        </li>
        <li>
          <svg viewBox="0 0 12 12" aria-hidden="true"><path d="M1 2.5h10v.9L6 6.6 1 3.4z"/><path d="M1 4.6l5 3.2 5-3.2v5H1z"/></svg>
          halyna@medmailbox.org.uk
        </li>
      </ul>
    </section>
  </main>
</body>
</html>
```